Business Card for Toffee Parlour

I have a logo for my candy buffet business, and need a business card designed using that logo. Toffee Parlour designs and builds beautiful and delicious candy and dessert tables for all kinds of events. The card should be simple, modern, graphic, colorful, and use the Toffee Parlour Logo.

Target Market(s)

The target market is people hosting major parties and events. This includes brides getting married, parents hosting birthday parties/Sweet Sixteen/Bar Mitzvah/quinceanera parties, and companies hosting corporate events.

Industry/Entity Type

Business

Requirements
Must have
• The business card must have the logo, with or without the tag line.

The following information must be on the card:

Renata Hollis
CEO & Candy Stylist
415.372.6091
renata@toffeeparlourco.example
Nice to have
• I like the idea of having multiple colors of the same design so that several people receiving cards will each receive a different color. Perhaps 3-5 colors or variations on a basic card design.

```html
<!DOCTYPE html>
<html lang="en">
<head>
<meta charset="utf-8">
<title>Toffee Parlour – Business Card</title>
<link rel="stylesheet" href="https://fonts.googleapis.com/css2?family=Questrial&family=Open+Sans:wght@400;700&display=swap">
<style>
  :root {
    --backdrop: #3b3735;
    --card: #ffffff;
    --pink: #ec1e84;
    --green: #4ab957;
    --ink: #231f20;
    --dot: #ec1e84;
  }
  * { box-sizing: border-box; margin: 0; padding: 0; }
  html, body { width: 1200px; height: 776px; overflow: hidden; }
  body {
    background: var(--backdrop);
    position: relative;
    font-family: "Open Sans", sans-serif;
    color: var(--ink);
  }
  .card {
    position: absolute;
    top: 226px;
    width: 540px;
    height: 324px;
    background: var(--card);
    overflow: hidden;
    box-shadow: 0 6px 18px rgba(0,0,0,.35);
  }
  .card--back { left: 40px; }
  .card--front { left: 620px; }

  /* contact side */
  .back-header { position: absolute; top: 0; left: 0; width: 540px; height: 50px; display: block; }
  .back-header__url {
    position: absolute; top: 10px; left: 22px;
    font-weight: 700; font-size: 12px; line-height: 16px;
    color: #fff; white-space: nowrap;
  }
  .holder { position: absolute; top: 42px; right: 26px; text-align: right; }
  .holder__name { font-family: "Questrial", sans-serif; font-size: 25px; line-height: 1; letter-spacing: -.3px; }
  .holder__title { font-size: 9px; margin-top: 6px; }
  .card--back .brand { position: absolute; left: 34px; top: 138px; }
  .contact {
    position: absolute; right: 34px; top: 240px;
    font-size: 11px; line-height: 1;
  }
  .contact__row { display: flex; align-items: center; gap: 6px; margin-bottom: 10px; white-space: nowrap; }
  .contact__row svg { width: 11px; height: 11px; flex: none; }
  .band--bottom-pink { position: absolute; left: 0; bottom: 0; width: 100%; height: 18px; background: var(--pink); }

  /* brand side */
  .band--top-pink { position: absolute; left: 0; top: 0; width: 100%; height: 22px; background: var(--pink); }
  .card--front .brand { position: absolute; left: 0; right: 0; top: 128px; justify-content: center; }
  .front-footer {
    position: absolute; left: 0; bottom: 0; width: 100%; height: 40px;
    background: var(--green); display: flex; justify-content: center;
  }
  .front-footer__url {
    width: 210px; height: 100%; background: var(--pink); color: #fff;
    font-weight: 700; font-size: 12px; white-space: nowrap;
    display: flex; align-items: center; justify-content: center;
  }

  /* brand name with a single plain circle */
  .brand { display: flex; align-items: center; gap: 12px; }
  .brand__mark { display: block; width: 30px; height: 30px; border-radius: 50%; background: var(--dot); flex: none; }
  .brand__name { font-size: 34px; font-weight: 400; line-height: 1; color: var(--ink); white-space: nowrap; }
  .card--front .brand__name { font-size: 40px; }
  .card--front .brand__mark { width: 34px; height: 34px; }
</style>
</head>
<body>

<section class="card card--back" aria-label="Business card, contact side">
  <svg class="back-header" viewBox="0 0 540 50" aria-hidden="true">
    <rect x="0" y="0" width="540" height="20" fill="var(--pink)"/>
    <path d="M0 0 H300 C278 4 268 16 256 26 C246 34 236 36 222 36 H0 Z" fill="var(--green)"/>
  </svg>
  <span class="back-header__url">www.toffeeparlourco.example</span>

  <div class="holder">
    <p class="holder__name">Renata Hollis</p>
    <p class="holder__title">CEO &amp; Candy Stylist</p>
  </div>

  <div class="brand">
    <span class="brand__mark"></span>
    <p class="brand__name">toffee parlour</p>
  </div>

  <div class="contact">
    <p class="contact__row">
      <svg viewBox="0 0 24 24" aria-hidden="true"><path fill="var(--pink)" d="M6.6 10.8a15 15 0 0 0 6.6 6.6l2.2-2.2c.3-.3.7-.4 1-.2 1.1.4 2.3.6 3.6.6.6 0 1 .4 1 1V20c0 .6-.4 1-1 1A17 17 0 0 1 3 4c0-.6.4-1 1-1h3.5c.6 0 1 .4 1 1 0 1.3.2 2.5.6 3.6.1.3 0 .7-.2 1z"/></svg>
      415.372.6091
    </p>
    <p class="contact__row">
      <svg viewBox="0 0 24 24" aria-hidden="true"><circle cx="12" cy="12" r="10" fill="none" stroke="var(--pink)" stroke-width="2"/><path d="M2 12h20M12 2c3 3 3 17 0 20M12 2c-3 3-3 17 0 20" fill="none" stroke="var(--pink)" stroke-width="2"/></svg>
      renata@toffeeparlourco.example
    </p>
  </div>

  <div class="band--bottom-pink"></div>
</section>

<section class="card card--front" aria-label="Business card, brand side">
  <div class="band--top-pink"></div>
  <div class="brand">
    <span class="brand__mark"></span>
    <p class="brand__name">toffee parlour</p>
  </div>
  <div class="front-footer">
    <span class="front-footer__url">www.toffeeparlourco.example</span>
  </div>
</section>

</body>
</html>
```